RWM Bricklaying business card

i need a business card designed for my bricklaying company.
I was also hoping to get a logo drawn up so i can put it on some t-shirts.
You can use any style or colours just as long as it lloks good. thanks Dalton

Industry/Entity Type

Business

Contact Information for Business Card

Dalton Briggs
RWM Bricklaying
0461937205
Any type of brick/blockwork
No job too small

```html
<!DOCTYPE html>
<html lang="en">
<head>
<meta charset="utf-8">
<title>RWM Bricklaying business card</title>
<link rel="stylesheet" href="https://fonts.googleapis.com/css2?family=Lato:wght@400;700;900&display=swap">
<style>
  :root {
    --backdrop: #e6e4e2;
    --card-black: #0b0b0b;
    --card-white: #ffffff;
    --brick-red: #c0272d;
    --ink: #1c1c1c;
    --muted: #333333;
  }
  * { box-sizing: border-box; margin: 0; padding: 0; }
  html, body {
    width: 1200px; height: 997px; overflow: hidden;
    background: var(--backdrop);
    font-family: "Lato", Arial, sans-serif;
  }
  .stage { position: relative; width: 1200px; height: 997px; }
  .card {
    position: absolute; width: 560px; height: 320px;
    box-shadow: 0 10px 28px rgba(0,0,0,0.18);
  }
  .card--front {
    left: 90px; top: 170px; background: var(--card-black);
    display: flex; align-items: center; justify-content: center;
  }
  .card--back {
    left: 550px; top: 500px; background: var(--card-white);
    overflow: hidden;
  }
  .wordmark { display: flex; align-items: center; gap: 12px; color: var(--brick-red); font-weight: 900; }
  .wordmark__square { width: 22px; height: 22px; background: var(--brick-red); }
  .wordmark__name { font-size: 40px; letter-spacing: 1px; line-height: 1; }
  .card--back .wordmark { position: absolute; left: 40px; top: 58px; }
  .card--back .wordmark__name { font-size: 30px; }
  .card--back .wordmark__square { width: 18px; height: 18px; }
  .company { position: absolute; left: 40px; top: 200px; }
  .company__name { color: var(--brick-red); font-weight: 700; font-size: 15px; margin-bottom: 5px; }
  .company__address { color: var(--ink); font-weight: 700; font-size: 13px; line-height: 1.55; }
  .person { position: absolute; right: 30px; top: 40px; text-align: right; }
  .person__name { color: var(--brick-red); font-weight: 700; font-size: 18px; }
  .person__title { color: var(--ink); font-weight: 700; font-size: 13px; margin-top: 2px; }
  .contacts { position: absolute; right: 30px; top: 130px; list-style: none; }
  .contacts li {
    display: flex; justify-content: flex-end; align-items: center; gap: 8px;
    color: var(--ink); font-weight: 700; font-size: 12.5px; height: 21px;
  }
  .contacts svg { width: 14px; height: 14px; flex: none; }
  .edge-band { position: absolute; left: 0; right: 0; bottom: 0; height: 12px; background: var(--card-black); }
</style>
</head>
<body>
<main class="stage">
  <section class="card card--front" aria-label="Business card front">
    <div class="wordmark">
      <span class="wordmark__square"></span>
      <span class="wordmark__name">RWM BRICKLAYING</span>
    </div>
  </section>

  <section class="card card--back" aria-label="Business card back">
    <div class="wordmark">
      <span class="wordmark__square"></span>
      <span class="wordmark__name">RWM BRICKLAYING</span>
    </div>

    <div class="company">
      <p class="company__name">RWM Bricklaying</p>
      <p class="company__address">Unit 18, 42 Mortar Lane,<br>NSW 12345</p>
    </div>

    <div class="person">
      <p class="person__name">Dalton Briggs</p>
      <p class="person__title">President</p>
    </div>

    <ul class="contacts">
      <li>0461 937 205
        <svg viewBox="0 0 14 14" aria-hidden="true"><circle cx="7" cy="7" r="7" fill="#c0272d"/><path d="M4.2 3.5l1.5-.3.8 1.8-.9.7c.4.9 1 1.5 1.9 1.9l.7-.9 1.8.8-.3 1.5c-3 .2-5.7-2.5-5.5-5.5z" fill="#fff"/></svg>
      </li>
      <li>0461 937 205
        <svg viewBox="0 0 14 14" aria-hidden="true"><circle cx="7" cy="7" r="7" fill="#c0272d"/><rect x="5" y="3" width="4" height="8" rx="0.8" fill="#fff"/></svg>
      </li>
      <li>dalton.b@rwmbricklaying.com.au
        <svg viewBox="0 0 14 14" aria-hidden="true"><circle cx="7" cy="7" r="7" fill="#c0272d"/><rect x="3.5" y="4.5" width="7" height="5" fill="#fff"/><path d="M3.5 4.5L7 7.3l3.5-2.8" stroke="#c0272d" stroke-width="0.8" fill="none"/></svg>
      </li>
      <li>www.rwmbricklaying.com.au
        <svg viewBox="0 0 14 14" aria-hidden="true"><circle cx="7" cy="7" r="7" fill="#c0272d"/><circle cx="7" cy="7" r="3.6" stroke="#fff" stroke-width="0.9" fill="none"/><path d="M3.4 7h7.2M7 3.4v7.2" stroke="#fff" stroke-width="0.8"/></svg>
      </li>
    </ul>

    <div class="edge-band"></div>
  </section>
</main>
</body>
</html>
```